Interactive Report Dashboard for Data Analytics

Please see this seekly doc for information and pictures regarding our project.
https://files.plomvex.com/doc/8TrwQ2mZpLx4VnKc0sYd7HjE3fRb9uNa5Gq/view?share=open
Feel free to message me if you have any questions.
Target Market(s)
This is for video producers, youtubers, and online teachers.
We run focus groups for them and help them understand how their audience reacts to the video content.
Coding
Coded - Design and coding required
Number of Pages Required
5+ page
Colors
Designer to choose colors to be used in the design.
Look and feel
Each slider illustrates characteristics of the customer's brand and the style your logo design should communicate.

```html
<!DOCTYPE html>
<html lang="en">
<head>
<meta charset="utf-8">
<title>Pulsera – Audience Report Dashboard</title>
<link href="https://fonts.googleapis.com/css2?family=Open+Sans:wght@400;600;700;800&display=swap" rel="stylesheet">
<style>
:root{
  --navy:#27308a;
  --accent:#d9531e;
  --orange:#cc4612;
  --panel:#f2f1f3;
  --card:#ffffff;
  --line:#dcdbe0;
  --ink:#222228;
  --muted:#6a6a72;
  --blue:#2d47c8;
  --red:#e0403a;
  --green:#3c9a3a;
}
*{box-sizing:border-box}
html,body{margin:0}
body{width:1200px;height:3005px;overflow:hidden;background:#fff;font-family:'Open Sans',sans-serif;color:var(--ink);position:relative}
.defs{position:absolute;width:0;height:0}

/* desktop screen */
.screen{position:absolute;left:48px;width:904px;background:var(--panel);box-shadow:0 1px 5px rgba(0,0,0,.18);display:flex;flex-direction:column;overflow:hidden}
.topbar{height:28px;flex:none;background:var(--navy);display:flex;align-items:center;justify-content:space-between;padding:0 12px;color:#fff}
.brand{font-weight:800;font-size:17px;letter-spacing:.2px}
.user{display:flex;align-items:center;gap:7px;font-size:10px;font-weight:600}
.avatar{width:16px;height:16px;border-radius:50%;background:linear-gradient(135deg,#9b8b78,#4a3e35)}
.icon{width:12px;height:12px;fill:none;stroke:#fff;stroke-width:1.6}
.subbar{height:30px;flex:none;background:#fff;border-bottom:1px solid var(--line);display:flex;align-items:center;font-size:9px}
.selected{width:174px;padding-left:14px;display:flex;gap:8px;align-items:center}
.sort{margin-left:auto;margin-right:24px;display:flex;align-items:center;gap:10px}
.select{width:170px;height:17px;border:1px solid var(--line);display:flex;align-items:center;justify-content:space-between;padding:0 6px;font-size:8.5px}
.body{flex:1;display:flex;min-height:0}

/* filters */
.filters{width:174px;flex:none;background:#fff;border-right:1px solid var(--line);padding:14px 12px}
.search{height:20px;border:1px solid var(--line);display:flex;align-items:center;justify-content:space-between;padding:0 6px;font-size:8.5px;color:var(--muted)}
.search svg{width:10px;height:10px;fill:none;stroke:#555;stroke-width:1.6}
.range{margin-top:14px;font-size:9.5px;font-weight:600}
.track{position:relative;height:2px;background:var(--accent);margin:9px 0 6px}
.thumb{position:absolute;top:-5px;width:11px;height:11px;border-radius:50%;background:var(--accent)}
.range-ends{display:flex;justify-content:space-between;font-size:6.5px;font-weight:400;color:var(--muted)}
.dropdown{margin-top:10px;height:22px;border:1px solid var(--line);display:flex;align-items:center;justify-content:space-between;padding:0 7px;font-size:8.5px;color:#444}
.dropdown:first-of-type{margin-top:18px}
.chev{width:8px;height:8px;fill:none;stroke:#666;stroke-width:1.5}

/* content */
.content{flex:1;padding:0 24px 0 14px;display:flex;flex-direction:column;min-width:0}
.tabs{display:flex;gap:32px;border-bottom:2px solid var(--line);margin-top:14px;font-size:9.5px;font-weight:700;color:#333}
.tab{padding:6px 0}
.tab.active{color:var(--navy);border-bottom:3px solid var(--navy);margin-bottom:-2px}
.site-footer{margin-top:auto;display:flex;justify-content:space-between;font-size:8.5px;color:#555;padding:10px 0 16px}
.site-footer nav span{margin:0 4px}

/* analytic cards */
.chart-grid{display:grid;grid-template-columns:repeat(3,166px);column-gap:72px;row-gap:26px;margin-top:18px}
.chart-card{position:relative}
.figure{height:144px;background:var(--card);box-shadow:0 1px 4px rgba(0,0,0,.14);display:block}
.figure svg{width:100%;height:100%;display:block}
.chart-card h3{font-size:9.5px;font-weight:800;margin:12px 0 3px}
.chart-card p{font-size:8.5px;line-height:1.35;margin:0;color:#333}
.expand{position:absolute;right:0;top:152px;width:10px;height:10px;fill:none;stroke:#555;stroke-width:1.4}
.map{background:radial-gradient(ellipse at 40% 45%,#2f8f2c,#6fbf5f 55%,#e8f1e6 80%)}

/* emotion display */
.videos{display:flex;gap:44px;margin:38px 0 0 26px}
.video{width:280px;height:172px;background:#111;position:relative;box-shadow:0 1px 4px rgba(0,0,0,.2)}
.frame{position:absolute;inset:0 0 20px 0}
.frame.dark{background:linear-gradient(90deg,#1b2230,#55503f 45%,#2a2622)}
.frame.field{background:linear-gradient(180deg,#c2bfb7,#9c8d74 55%,#4f4536)}
.meters{position:absolute;left:92px;bottom:32px;display:flex;gap:14px;align-items:flex-end}
.meter{width:36px;font-size:6.5px;color:#fff;text-align:center}
.meter i{display:block;width:6px;margin:0 auto 2px;background:#7ed6a5}
.wave{position:absolute;left:0;right:0;bottom:22px;height:40px}
.controls{position:absolute;left:0;right:0;bottom:0;height:20px;background:#1a1a1a;display:flex;align-items:center;gap:8px;padding:0 8px}
.controls .bar{flex:1;height:2px;background:#666}
.controls b{width:6px;height:8px;background:#ddd}

/* survey */
.survey-tabs{margin-top:20px;display:grid;grid-template-columns:repeat(4,1fr);background:#fff;border:1px solid var(--line);font-size:9px;font-weight:600}
.survey-tabs span{height:34px;display:flex;align-items:center;justify-content:center;text-align:center;border-right:1px solid var(--line)}
.survey-tabs .on{background:var(--navy);color:#fff}
.mode{display:flex;background:#e3e2e5;font-size:8px;font-weight:700}
.mode span{width:186px;height:22px;display:flex;align-items:center;justify-content:center}
.mode .on{background:var(--orange);color:#fff}
.survey h2{font-size:13px;font-weight:800;margin:18px 0 10px;letter-spacing:.2px}
.resp-grid{display:grid;grid-template-columns:repeat(3,1fr);gap:12px 20px}
.resp{background:#fff;box-shadow:0 1px 4px rgba(0,0,0,.12);padding:16px 18px;min-width:0}
.resp h4{margin:0 0 10px;font-size:12px;font-weight:800}
.resp p{margin:0;font-size:9.5px;line-height:1.45;color:#333}
.q-grid{display:grid;grid-template-columns:repeat(2,1fr);gap:16px 12px;margin-top:16px}
.question{background:#fff;box-shadow:0 1px 4px rgba(0,0,0,.12);height:204px;padding:14px 18px;min-width:0;overflow:hidden}
.question p{margin:0 0 8px;font-size:9.5px;line-height:1.4}
.question svg{width:300px;height:120px;max-width:100%}

/* mobile */
.mobile{position:absolute;left:996px;top:48px;width:168px;height:1980px;background:var(--panel);box-shadow:0 1px 5px rgba(0,0,0,.18);overflow:hidden;display:flex;flex-direction:column}
.mobile .topbar{height:24px;padding:0 8px}
.mobile .brand{font-size:13px}
.mobile .subbar{height:22px;font-size:7px;padding:0 6px;justify-content:space-between}
.mobile .select{width:56px;height:12px;font-size:6.5px}
.mobile .filters{width:auto;border:0;padding:10px 10px 14px}
.mobile .dropdown{height:18px;font-size:7px;margin-top:9px}
.mobile .range{font-size:8px;margin-top:12px}
.mobile .search{font-size:7px;height:17px}
.m-tabs{background:#fff;font-size:7.5px;font-weight:700;text-align:center;border-top:1px solid var(--line)}
.m-tabs div{padding:10px 0;border-bottom:1px solid var(--line)}
.m-tabs .active{color:var(--navy);border-bottom:3px solid var(--navy);background:#ecebf3}
.m-cards{padding:10px 12px 0}
.m-card{position:relative;height:156px}
.m-card .figure{height:106px}
.m-card h3{font-size:6.5px;font-weight:800;margin:7px 0 2px}
.m-card p{font-size:6px;line-height:1.3;margin:0}
.m-card .expand{top:110px;width:8px;height:8px}
.m-footer{margin-top:auto;text-align:center;font-size:7px;color:#555;padding:0 0 22px;line-height:2}
</style>
</head>
<body>

<svg class="defs" aria-hidden="true">
  <defs>
    <symbol id="ic-search" viewBox="0 0 12 12"><circle cx="5" cy="5" r="3.6"/><path d="M7.7 7.7L11 11"/></symbol>
    <symbol id="ic-chev" viewBox="0 0 10 10"><path d="M2 3.5l3 3 3-3"/></symbol>
    <symbol id="ic-expand" viewBox="0 0 12 12"><path d="M7 1h4v4M11 1L7 5M5 11H1V7M1 11l4-4"/></symbol>
    <symbol id="ic-gear" viewBox="0 0 12 12"><circle cx="6" cy="6" r="2"/><circle cx="6" cy="6" r="4.6" stroke-dasharray="2 1.6"/></symbol>
    <symbol id="ic-bell" viewBox="0 0 12 12"><path d="M3 8.5V5.5a3 3 0 016 0v3l1 1H2zM5 10.5h2"/></symbol>

    <symbol id="c-scatter" viewBox="0 0 166 144">
      <text x="10" y="14" font-size="5.5" fill="#333">Age vs. Weight comparison</text>
      <path d="M16 22v104h140" stroke="#bbb" fill="none"/>
      <g fill="#4a3fa8"><circle cx="40" cy="110" r="2"/><circle cx="52" cy="98" r="2"/><circle cx="66" cy="84" r="2"/><circle cx="82" cy="90" r="2"/><circle cx="98" cy="60" r="2"/><circle cx="118" cy="54" r="2"/><circle cx="60" cy="104" r="2"/></g>
    </symbol>
    <symbol id="c-hist" viewBox="0 0 166 144">
      <text x="10" y="14" font-size="5.5" fill="#333">Length distribution, in meters</text>
      <path d="M16 22v104h140" stroke="#bbb" fill="none"/>
      <g fill="#2d47c8"><rect x="18" y="28" width="14" height="98"/><rect x="33" y="46" width="14" height="80"/><rect x="48" y="64" width="14" height="62"/><rect x="63" y="82" width="14" height="44"/><rect x="78" y="100" width="14" height="26"/><rect x="93" y="112" width="14" height="14"/><rect x="108" y="118" width="14" height="8"/><rect x="123" y="120" width="14" height="6"/><rect x="138" y="122" width="14" height="4"/></g>
    </symbol>
    <symbol id="c-hbar" viewBox="0 0 166 144">
      <text x="34" y="14" font-size="6" fill="#333" font-weight="700">Population of Largest U.S. Cities</text>
      <g font-size="5" fill="#333" text-anchor="end"><text x="42" y="34">New York City, NY</text><text x="42" y="54">Los Angeles, CA</text><text x="42" y="74">Chicago, IL</text><text x="42" y="94">Houston, TX</text><text x="42" y="114">Philadelphia, PA</text></g>
      <path d="M44 22v102h114" stroke="#bbb" fill="none"/>
      <g fill="#e0403a"><rect x="44" y="27" width="108" height="5"/><rect x="44" y="47" width="56" height="5"/><rect x="44" y="67" width="40" height="5"/><rect x="44" y="87" width="32" height="5"/><rect x="44" y="107" width="22" height="5"/></g>
      <g fill="#2d47c8"><rect x="44" y="33" width="114" height="5"/><rect x="44" y="53" width="60" height="5"/><rect x="44" y="73" width="42" height="5"/><rect x="44" y="93" width="34" height="5"/><rect x="44" y="113" width="24" height="5"/></g>
      <text x="100" y="136" font-size="5" fill="#333" text-anchor="middle">Total Population</text>
    </symbol>
    <symbol id="c-pie" viewBox="0 0 166 144">
      <g transform="rotate(-90 66 72)" fill="none" stroke-width="52">
        <circle cx="66" cy="72" r="26" stroke="#2d47c8" stroke-dasharray="68.6 163.4"/>
        <circle cx="66" cy="72" r="26" stroke="#3c9a3a" stroke-dasharray="14.7 163.4" stroke-dashoffset="-68.6"/>
        <circle cx="66" cy="72" r="26" stroke="#f0a020" stroke-dasharray="9.8 163.4" stroke-dashoffset="-83.3"/>
        <circle cx="66" cy="72" r="26" stroke="#e0403a" stroke-dasharray="16.3 163.4" stroke-dashoffset="-93.1"/>
        <circle cx="66" cy="72" r="26" stroke="#8a1f9a" stroke-dasharray="54 163.4" stroke-dashoffset="-109.4"/>
      </g>
      <g font-size="5" fill="#333"><rect x="128" y="32" width="5" height="5" fill="#2d47c8"/><text x="136" y="37">Work</text><rect x="128" y="42" width="5" height="5" fill="#3c9a3a"/><text x="136" y="47">Eat</text><rect x="128" y="52" width="5" height="5" fill="#f0a020"/><text x="136" y="57">Commute</text><rect x="128" y="62" width="5" height="5" fill="#e0403a"/><text x="136" y="67">Watch TV</text><rect x="128" y="72" width="5" height="5" fill="#8a1f9a"/><text x="136" y="77">Sleep</text></g>
    </symbol>
    <symbol id="c-bubble" viewBox="0 0 166 144">
      <text x="10" y="14" font-size="5" fill="#333">Correlation between life expectancy and income</text>
      <path d="M16 22v104h120" stroke="#bbb" fill="none"/>
      <circle cx="40" cy="96" r="6" fill="#e0403a" opacity=".8"/><circle cx="64" cy="86" r="9" fill="#f0a020" opacity=".8"/><circle cx="72" cy="60" r="5" fill="#f0a020" opacity=".8"/><circle cx="100" cy="80" r="10" fill="#2d47c8" opacity=".8"/><circle cx="120" cy="70" r="7" fill="#f0a020" opacity=".8"/><circle cx="118" cy="96" r="5" fill="#e0403a" opacity=".8"/>
      <g font-size="5" fill="#333"><circle cx="144" cy="30" r="2" fill="#2d47c8"/><text x="148" y="32">Asia</text><circle cx="144" cy="38" r="2" fill="#f0a020"/><text x="148" y="40">Europe</text><circle cx="144" cy="46" r="2" fill="#e0403a"/><text x="148" y="48">Africa</text></g>
    </symbol>
    <symbol id="c-tree" viewBox="0 0 166 144">
      <rect x="10" y="12" width="54" height="120" fill="#a9d3a0"/><rect x="65" y="12" width="44" height="120" fill="#e8a6a6"/><rect x="110" y="12" width="46" height="54" fill="#bfe0b6"/><rect x="110" y="67" width="46" height="65" fill="#d3ecca"/><rect x="10" y="12" width="146" height="6" fill="#2f8f2c"/><rect x="130" y="12" width="26" height="6" fill="#e0403a"/>
    </symbol>
    <symbol id="c-area" viewBox="0 0 166 144">
      <text x="10" y="14" font-size="5.5" fill="#333">Company Performance</text>
      <path d="M16 22v104h140" stroke="#bbb" fill="none"/>
      <path d="M16 126V96l40-30 40 40 58-70v90z" fill="#7f95e0" opacity=".7"/>
      <path d="M16 126V100l40 6 36-62 32 56 30-20v46z" fill="#e8908c" opacity=".7"/>
    </symbol>
    <symbol id="c-sankey" viewBox="0 0 166 144">
      <g fill="#bdbdbd" opacity=".85"><path d="M12 20h6c60 0 70 40 136 40v14c-66 0-76-40-136-40h-6z"/><path d="M12 44h6c60 0 70-20 136-20v14c-66 0-76 20-136 20h-6z"/><path d="M12 70h6c60 0 70 30 136 30v16c-66 0-76-30-136-30h-6z"/><path d="M12 96h6c60 0 70-14 136-14v12c-66 0-76 16-136 16h-6z"/></g>
      <rect x="8" y="18" width="4" height="96" fill="#888"/><rect x="154" y="22" width="4" height="20" fill="#8a1f9a"/><rect x="154" y="58" width="4" height="24" fill="#3c9a3a"/><rect x="154" y="84" width="4" height="34" fill="#f0a020"/>
    </symbol>

    <symbol id="c-survey" viewBox="0 0 300 120">
      <text x="0" y="8" font-size="5" fill="#333">Response share by answer band, all participants</text>
      <g font-size="5" fill="#333" text-anchor="end"><text x="28" y="34">0-20%</text><text x="28" y="50">20-40%</text><text x="28" y="66">40-60%</text><text x="28" y="82">60-80%</text><text x="28" y="98">80-100%</text></g>
      <path d="M32 18v88h120" stroke="#ccc" fill="none"/>
      <g fill="currentColor"><rect x="32" y="22" width="52" height="5"/><rect x="32" y="29" width="66" height="5" opacity=".7"/><rect x="32" y="38" width="80" height="5"/><rect x="32" y="45" width="60" height="5" opacity=".7"/><rect x="32" y="54" width="98" height="5"/><rect x="32" y="61" width="110" height="5" opacity=".7"/><rect x="32" y="70" width="70" height="5"/><rect x="32" y="77" width="48" height="5" opacity=".7"/><rect x="32" y="86" width="40" height="5"/><rect x="32" y="93" width="28" height="5" opacity=".7"/></g>
      <g font-size="5" fill="#444"><text x="180" y="30">0-20%</text><text x="220" y="30">12%</text><text x="180" y="44">20-40%</text><text x="220" y="44">18%</text><text x="180" y="58">40-60%</text><text x="220" y="58">34%</text><text x="180" y="72">60-80%</text><text x="220" y="72">22%</text><text x="180" y="86">80-100%</text><text x="220" y="86">14%</text></g>
      <path d="M176 34h70M176 48h70M176 62h70M176 76h70" stroke="#eee"/>
      <g font-size="5" fill="#666"><text x="30" y="114">0</text><text x="70" y="114">10</text><text x="110" y="114">20</text><text x="148" y="114">30</text></g>
    </symbol>
  </defs>
</svg>

<!-- Screen: audience analytic tools -->
<section class="screen" style="top:48px;height:876px">
  <header class="topbar"><span class="brand">Pulsera</span><div class="user">Hello, Marcus <svg class="icon"><use href="#ic-chev"/></svg><span class="avatar" role="img" aria-label="User profile photo"></span><svg class="icon"><use href="#ic-gear"/></svg><svg class="icon"><use href="#ic-bell"/></svg></div></header>
  <div class="subbar"><span class="selected"><svg class="chev"><use href="#ic-chev"/></svg>0 Selected</span><span class="sort">Sort By <span class="select">View All <svg class="chev"><use href="#ic-chev"/></svg></span></span></div>
  <div class="body">
    <aside class="filters">
      <div class="search">Keyword <svg><use href="#ic-search"/></svg></div>
      <div class="range">Age<div class="track"><span class="thumb" style="left:12%"></span></div><div class="range-ends"><span>15</span><span>80</span></div></div>
      <div class="range">Income<div class="track"><span class="thumb" style="left:22%"></span></div><div class="range-ends"><span>$10K</span><span>$100K</span></div></div>
      <div class="dropdown">Nationality <svg class="chev"><use href="#ic-chev"/></svg></div>
      <div class="dropdown">Education <svg class="chev"><use href="#ic-chev"/></svg></div>
      <div class="dropdown">Gender <svg class="chev"><use href="#ic-chev"/></svg></div>
      <div class="dropdown">Intrests <svg class="chev"><use href="#ic-chev"/></svg></div>
      <div class="dropdown">Personalities <svg class="chev"><use href="#ic-chev"/></svg></div>
    </aside>
    <main class="content">
      <nav class="tabs"><span class="tab active">AUDIENCE ANALYTIC TOOLS</span><span class="tab">REAL TIME EMOTION DISPLAY</span><span class="tab">SURVEY RESPONSES</span></nav>
      <div class="chart-grid">
        <article class="chart-card"><div class="figure map" role="img" aria-label="World map shaded by audience location"></div><svg class="expand"><use href="#ic-expand"/></svg><h3>LOREM IPSUM IS SIMPLY</h3><p>Contrary to popular belief, Lorem Ipsum is not simply random text. It has roots in a piece</p></article>
        <article class="chart-card"><div class="figure"><svg><use href="#c-scatter"/></svg></div><svg class="expand"><use href="#ic-expand"/></svg><h3>LOREM IPSUM IS SIMPLY</h3><p>Contrary to popular belief, Lorem Ipsum is not simply random text. It has roots in a piece</p></article>
        <article class="chart-card"><div class="figure"><svg><use href="#c-hist"/></svg></div><svg class="expand"><use href="#ic-expand"/></svg><h3>LOREM IPSUM IS SIMPLY</h3><p>Contrary to popular belief, Lorem Ipsum is not simply random text. It has roots in a piece</p></article>
        <article class="chart-card"><div class="figure"><svg><use href="#c-hbar"/></svg></div><svg class="expand"><use href="#ic-expand"/></svg><h3>LOREM IPSUM IS SIMPLY</h3><p>Contrary to popular belief, Lorem Ipsum is not simply random text. It has roots in a piece</p></article>
        <article class="chart-card"><div class="figure"><svg><use href="#c-pie"/></svg></div><svg class="expand"><use href="#ic-expand"/></svg><h3>LOREM IPSUM IS SIMPLY</h3><p>Contrary to popular belief, Lorem Ipsum is not simply random text. It has roots in a piece</p></article>
        <article class="chart-card"><div class="figure"><svg><use href="#c-bubble"/></svg></div><svg class="expand"><use href="#ic-expand"/></svg><h3>LOREM IPSUM IS SIMPLY</h3><p>Contrary to popular belief, Lorem Ipsum is not simply random text. It has roots in a piece</p></article>
        <article class="chart-card"><div class="figure"><svg><use href="#c-tree"/></svg></div><svg class="expand"><use href="#ic-expand"/></svg><h3>LOREM IPSUM IS SIMPLY</h3><p>Contrary to popular belief, Lorem Ipsum is not simply random text. It has roots in a piece</p></article>
        <article class="chart-card"><div class="figure"><svg><use href="#c-area"/></svg></div><svg class="expand"><use href="#ic-expand"/></svg><h3>LOREM IPSUM IS SIMPLY</h3><p>Contrary to popular belief, Lorem Ipsum is not simply random text. It has roots in a piece</p></article>
        <article class="chart-card"><div class="figure"><svg><use href="#c-sankey"/></svg></div><svg class="expand"><use href="#ic-expand"/></svg><h3>LOREM IPSUM IS SIMPLY</h3><p>Contrary to popular belief, Lorem Ipsum is not simply random text. It has roots in a piece</p></article>
      </div>
      <footer class="site-footer"><nav>About Us<span>|</span>FAQ<span>|</span>Terms &amp; Conditions<span>|</span>Feedback</nav><span>Copyrights @ 2018 All Rights Reserved</span></footer>
    </main>
  </div>
</section>

<!-- Screen: real time emotion display -->
<section class="screen" style="top:968px;height:468px">
  <header class="topbar"><span class="brand">Pulsera</span><div class="user">Hello, Marcus <svg class="icon"><use href="#ic-chev"/></svg><span class="avatar" role="img" aria-label="User profile photo"></span><svg class="icon"><use href="#ic-gear"/></svg><svg class="icon"><use href="#ic-bell"/></svg></div></header>
  <div class="subbar"><span class="selected"><svg class="chev"><use href="#ic-chev"/></svg>0 Selected</span><span class="sort">Sort By <span class="select">View All <svg class="chev"><use href="#ic-chev"/></svg></span></span></div>
  <div class="body">
    <aside class="filters">
      <div class="search">Keyword <svg><use href="#ic-search"/></svg></div>
      <div class="range">Age<div class="track"><span class="thumb" style="left:12%"></span></div><div class="range-ends"><span>15</span><span>80</span></div></div>
      <div class="range">Income<div class="track"><span class="thumb" style="left:22%"></span></div><div class="range-ends"><span>$10K</span><span>$100K</span></div></div>
      <div class="dropdown">Nationality <svg class="chev"><use href="#ic-chev"/></svg></div>
      <div class="dropdown">Education <svg class="chev"><use href="#ic-chev"/></svg></div>
      <div class="dropdown">Gender <svg class="chev"><use href="#ic-chev"/></svg></div>
      <div class="dropdown">Intrests <svg class="chev"><use href="#ic-chev"/></svg></div>
      <div class="dropdown">Personalities <svg class="chev"><use href="#ic-chev"/></svg></div>
    </aside>
    <main class="content">
      <nav class="tabs"><span class="tab">AUDIENCE ANALYTIC TOOLS</span><span class="tab active">REAL TIME EMOTION DISPLAY</span><span class="tab">SURVEY RESPONSES</span></nav>
      <div class="videos">
        <div class="video">
          <div class="frame dark" role="img" aria-label="Video still of a dramatic indoor film scene"></div>
          <div class="meters"><div class="meter"><i style="height:26px"></i>Engagement</div><div class="meter"><i style="height:14px;background:#f2c14e"></i>Disgust</div><div class="meter"><i style="height:20px;background:#e88"></i>Fear</div></div>
          <div class="controls"><b></b><span class="bar"></span><b></b><b></b></div>
        </div>
        <div class="video">
          <div class="frame field" role="img" aria-label="Video still of an outdoor action film scene"></div>
          <svg class="wave" viewBox="0 0 280 40" preserveAspectRatio="none"><path d="M0 30C30 10 50 36 80 22s50 10 80-8 50 20 80 6 30 6 40 2" fill="none" stroke="#e0403a" stroke-width="1.5"/><path d="M0 34C40 26 60 30 100 28s60-6 90 0 60 4 90-2" fill="none" stroke="#7ed6a5" stroke-width="1.2"/></svg>
          <div class="controls"><b></b><span class="bar"></span><b></b><b></b></div>
        </div>
      </div>
      <footer class="site-footer"><nav>About Us<span>|</span>FAQ<span>|</span>Terms &amp; Conditions<span>|</span>Feedback</nav><span>Copyrights @ 2018 All Rights Reserved</span></footer>
    </main>
  </div>
</section>

<!-- Screen: survey, single choice -->
<section class="screen" style="top:1480px;height:712px">
  <header class="topbar"><span class="brand">Pulsera</span><div class="user">Hello, Marcus <svg class="icon"><use href="#ic-chev"/></svg><span class="avatar" role="img" aria-label="User profile photo"></span><svg class="icon"><use href="#ic-gear"/></svg><svg class="icon"><use href="#ic-bell"/></svg></div></header>
  <div class="subbar"><span class="selected"><svg class="chev"><use href="#ic-chev"/></svg>0 Selected</span><span class="sort">Sort By <span class="select">View All <svg class="chev"><use href="#ic-chev"/></svg></span></span></div>
  <div class="body">
    <aside class="filters">
      <div class="search">Keyword <svg><use href="#ic-search"/></svg></div>
      <div class="range">Age<div class="track"><span class="thumb" style="left:12%"></span></div><div class="range-ends"><span>15</span><span>80</span></div></div>
      <div class="range">Income<div class="track"><span class="thumb" style="left:22%"></span></div><div class="range-ends"><span>$10K</span><span>$100K</span></div></div>
      <div class="dropdown">Nationality <svg class="chev"><use href="#ic-chev"/></svg></div>
      <div class="dropdown">Education <svg class="chev"><use href="#ic-chev"/></svg></div>
      <div class="dropdown">Gender <svg class="chev"><use href="#ic-chev"/></svg></div>
      <div class="dropdown">Intrests <svg class="chev"><use href="#ic-chev"/></svg></div>
      <div class="dropdown">Personalities <svg class="chev"><use href="#ic-chev"/></svg></div>
    </aside>
    <main class="content survey">
      <nav class="tabs"><span class="tab">AUDIENCE ANALYTIC TOOLS</span><span class="tab">REAL TIME EMOTION DISPLAY</span><span class="tab active">SURVEY RESPONSES</span></nav>
      <div class="survey-tabs"><span class="on">Personality Test Question Responses</span><span>Demography Question Responses</span><span>Political Question Responses</span><span>Client's Custom Question Responses</span></div>
      <div class="mode"><span class="on">SINGLE CHOICE QUESTIONS</span><span>MULTIPLE CHOICE QUESTIONS</span></div>
      <h2>HOW AFFECTED BY CRISIS</h2>
      <div class="resp-grid">
        <article class="resp" style="height:144px"><h4>RESP002</h4><p>Not really much. Well our cheaper carparking tickets have gone now. They withdrew concessionary tickets so its more difficult to get into town for the things I need.</p></article>
        <article class="resp"><h4>RESP003</h4><p>Completely. Really changed my customer base.</p></article>
        <article class="resp"><h4>RESP004</h4><p>Very attach. I had several jobs lined up and half of them have just disappeared.</p></article>
        <article class="resp" style="height:108px"><h4>RESP005</h4><p>Personally no but my family is affected</p></article>
        <article class="resp"><h4>RESP006</h4><p>I've got a private pension- lower in value the longer I wait before taking it.</p></article>
        <article class="resp"><h4>RESP007</h4><p>Mainly I worry about the kids.</p></article>
        <article class="resp" style="height:142px"><h4>RESP008</h4><p>My job is OK - but theres a pay freeze. Pity the rail fares don't freeze as well. I ammore worried about my grownup children and how they will cope.</p></article>
        <article class="resp"><h4>RESP009</h4><p>I got made redundant timths ago. That was awful. I am trying to get going with an idea I have but getting a small start-up business loan has been impossible. I'm caught by being my age - not getting my pension and not getting a bank loan either.</p></article>
      </div>
      <footer class="site-footer"><nav>About Us<span>|</span>FAQ<span>|</span>Terms &amp; Conditions<span>|</span>Feedback</nav><span>Copyrights @ 2018 All Rights Reserved</span></footer>
    </main>
  </div>
</section>

<!-- Screen: survey, multiple choice -->
<section class="screen" style="top:2236px;height:700px">
  <header class="topbar"><span class="brand">Pulsera</span><div class="user">Hello, Marcus <svg class="icon"><use href="#ic-chev"/></svg><span class="avatar" role="img" aria-label="User profile photo"></span><svg class="icon"><use href="#ic-gear"/></svg><svg class="icon"><use href="#ic-bell"/></svg></div></header>
  <div class="subbar"><span class="selected"><svg class="chev"><use href="#ic-chev"/></svg>0 Selected</span><span class="sort">Sort By <span class="select">View All <svg class="chev"><use href="#ic-chev"/></svg></span></span></div>
  <div class="body">
    <aside class="filters">
      <div class="search">Keyword <svg><use href="#ic-search"/></svg></div>
      <div class="range">Age<div class="track"><span class="thumb" style="left:12%"></span></div><div class="range-ends"><span>15</span><span>80</span></div></div>
      <div class="range">Income<div class="track"><span class="thumb" style="left:22%"></span></div><div class="range-ends"><span>$10K</span><span>$100K</span></div></div>
      <div class="dropdown">Nationality <svg class="chev"><use href="#ic-chev"/></svg></div>
      <div class="dropdown">Education <svg class="chev"><use href="#ic-chev"/></svg></div>
      <div class="dropdown">Gender <svg class="chev"><use href="#ic-chev"/></svg></div>
      <div class="dropdown">Intrests <svg class="chev"><use href="#ic-chev"/></svg></div>
      <div class="dropdown">Personalities <svg class="chev"><use href="#ic-chev"/></svg></div>
    </aside>
    <main class="content survey">
      <nav class="tabs"><span class="tab">AUDIENCE ANALYTIC TOOLS</span><span class="tab">REAL TIME EMOTION DISPLAY</span><span class="tab active">SURVEY RESPONSES</span></nav>
      <div class="survey-tabs"><span class="on">Personality Test Question Responses</span><span>Demography Question Responses</span><span>Political Question Responses</span><span>Client's Custom Question Responses</span></div>
      <div class="mode"><span>SINGLE CHOICE QUESTIONS</span><span class="on">MULTIPLE CHOICE QUESTIONS</span></div>
      <div class="q-grid">
        <article class="question"><p>In your opinion, what would be a weight age distribution for skills necessary for securing your dream job.(assuming you are a student)? Making your own stuff (apps,robots,anything)</p><svg style="color:#d8313a"><use href="#c-survey"/></svg></article>
        <article class="question"><p>How much does each of the following factors contribute to your learning? Books</p><svg style="color:#e3c61c"><use href="#c-survey"/></svg></article>
        <article class="question"><p>How much does each of the following factors contribute to your learning?-Teachers (Course instructors,teaching assistents,tutors)</p><svg style="color:#32c02c"><use href="#c-survey"/></svg></article>
        <article class="question"><p>How much does each of the following factors contribute to your learning? Online resources (Knowlpedia,seekly,social networks)</p><svg style="color:#9a2ea8"><use href="#c-survey"/></svg></article>
      </div>
      <footer class="site-footer"><nav>About Us<span>|</span>FAQ<span>|</span>Terms &amp; Conditions<span>|</span>Feedback</nav><span>Copyrights @ 2018 All Rights Reserved</span></footer>
    </main>
  </div>
</section>

<!-- Mobile: audience analytic tools -->
<section class="mobile">
  <header class="topbar"><span class="brand">Pulsera</span><div class="user"><span class="avatar" role="img" aria-label="User profile photo" style="width:12px;height:12px"></span><svg class="icon" style="width:10px;height:10px"><use href="#ic-gear"/></svg><svg class="icon" style="width:10px;height:10px"><use href="#ic-bell"/></svg></div></header>
  <div class="subbar"><span>⌄ 0 Selected</span><span>Sort By</span><span class="select">View All</span></div>
  <aside class="filters">
    <div class="search">Keyword <svg><use href="#ic-search"/></svg></div>
    <div class="range">Age<div class="track"><span class="thumb" style="left:12%"></span></div><div class="range-ends"><span>15</span><span>80</span></div></div>
    <div class="range">Income<div class="track"><span class="thumb" style="left:22%"></span></div><div class="range-ends"><span>$10K</span><span>$100K</span></div></div>
    <div class="dropdown">Nationality <svg class="chev"><use href="#ic-chev"/></svg></div>
    <div class="dropdown">Education <svg class="chev"><use href="#ic-chev"/></svg></div>
    <div class="dropdown">Gender <svg class="chev"><use href="#ic-chev"/></svg></div>
    <div class="dropdown">Intrests <svg class="chev"><use href="#ic-chev"/></svg></div>
    <div class="dropdown">Personalities <svg class="chev"><use href="#ic-chev"/></svg></div>
  </aside>
  <nav class="m-tabs"><div class="active">AUDIENCE ANALYTIC TOOLS</div><div>REAL TIME EMOTION DISPLAY</div><div>SURVEY RESPONSES</div></nav>
  <div class="m-cards">
    <article class="m-card"><div class="figure map" role="img" aria-label="World map shaded by audience location"></div><svg class="expand"><use href="#ic-expand"/></svg><h3>LOREM IPSUM IS SIMPLY</h3><p>Contrary to popular belief, Lorem Ipsum is not simply random text. It has roots in a piece</p></article>
    <article class="m-card"><div class="figure"><svg viewBox="0 0 166 144" preserveAspectRatio="none"><use href="#c-scatter"/></svg></div><svg class="expand"><use href="#ic-expand"/></svg><h3>LOREM IPSUM IS SIMPLY</h3><p>Contrary to popular belief, Lorem Ipsum is not simply random text. It has roots in a piece</p></article>
    <article class="m-card"><div class="figure"><svg viewBox="0 0 166 144" preserveAspectRatio="none"><use href="#c-hist"/></svg></div><svg class="expand"><use href="#ic-expand"/></svg><h3>LOREM IPSUM IS SIMPLY</h3><p>Contrary to popular belief, Lorem Ipsum is not simply random text. It has roots in a piece</p></article>
    <article class="m-card"><div class="figure"><svg viewBox="0 0 166 144" preserveAspectRatio="none"><use href="#c-hbar"/></svg></div><svg class="expand"><use href="#ic-expand"/></svg><h3>LOREM IPSUM IS SIMPLY</h3><p>Contrary to popular belief, Lorem Ipsum is not simply random text. It has roots in a piece</p></article>
    <article class="m-card"><div class="figure"><svg viewBox="0 0 166 144" preserveAspectRatio="none"><use href="#c-pie"/></svg></div><svg class="expand"><use href="#ic-expand"/></svg><h3>LOREM IPSUM IS SIMPLY</h3><p>Contrary to popular belief, Lorem Ipsum is not simply random text. It has roots in a piece</p></article>
    <article class="m-card"><div class="figure"><svg viewBox="0 0 166 144" preserveAspectRatio="none"><use href="#c-bubble"/></svg></div><svg class="expand"><use href="#ic-expand"/></svg><h3>LOREM IPSUM IS SIMPLY</h3><p>Contrary to popular belief, Lorem Ipsum is not simply random text. It has roots in a piece</p></article>
    <article class="m-card"><div class="figure"><svg viewBox="0 0 166 144" preserveAspectRatio="none"><use href="#c-tree"/></svg></div><svg class="expand"><use href="#ic-expand"/></svg><h3>LOREM IPSUM IS SIMPLY</h3><p>Contrary to popular belief, Lorem Ipsum is not simply random text. It has roots in a piece</p></article>
    <article class="m-card"><div class="figure"><svg viewBox="0 0 166 144" preserveAspectRatio="none"><use href="#c-area"/></svg></div><svg class="expand"><use href="#ic-expand"/></svg><h3>LOREM IPSUM IS SIMPLY</h3><p>Contrary to popular belief, Lorem Ipsum is not simply random text. It has roots in a piece</p></article>
    <article class="m-card"><div class="figure"><svg viewBox="0 0 166 144" preserveAspectRatio="none"><use href="#c-sankey"/></svg></div><svg class="expand"><use href="#ic-expand"/></svg><h3>LOREM IPSUM IS SIMPLY</h3><p>Contrary to popular belief, Lorem Ipsum is not simply random text. It has roots in a piece</p></article>
  </div>
  <footer class="m-footer">About Us &nbsp;|&nbsp; FAQ<br>Terms &amp; Conditions &nbsp;|&nbsp; Feedback<br>Copyrights @ 2018 All Rights Reserved</footer>
</section>

</body>
</html>
```